Copper Ridge Garage Door Sales & Repair needs a Business Card Design

I need a business card design to go with our new business logo that was created a few months ago.

Copper Ridge Garage Door specializes in selling and installing new garage doors, and new garage door openers. We also take care of all repairs to existing garage doors and garage door openers. All makes and models.

Target Market(s)

Home-owners, renters, anyone who lives in a house and has a garage. Residential and commercial garages.

Industry/Entity Type

Home Improvement

Contact Information for Business Card

I would like the business cards to have rounded corners and be double-sided. My old logo is still on my website at www.copperridgegarage.example. If I was going to incorporate a secondary color on the business cards, I think that orange is a good choice (especially since blue and orange are the colors of our Tulsa Comets), but I'm not opposed to seeing a different color if another color works better with my logo colors. I have two logo colors. One designed for a white background and one designed for a darker background. I'm not opposed to using both. Maybe a dark background with the white logo on one side, and a white background with the other logo color on the other side.

My business is a small, locally owned business that I am trying to grow. But I would like my business cards to look very professional. Like we have been in business for a long time. I like traditional to modern looking cards. Just something bold and memorable. My full company name is Copper Ridge Garage Door Sales & Repair. But you can just do COPPER RIDGE GARAGE DOOR, if that works better.

Font styles to use
Serif
Script

Requirements
Must have
• Rounded corners
• Double-sided
• 3-D Elements. Layering of some sort (a sketch of a garage door or a 3rd color (orange) brought in some how. I really like watermarks.
• Matte cards that you can write on.
• White on one side. (Or the lighter blue in my logo). Darker blue logo color on the other side.
• I would like our tag line on the cards somewhere... "For All Your Garage Door Needs".
• I would also like "Call For a FREE Estimate" by the phone number.
• And "Serving the Greater Metro Denver Area" somewhere on the card as well.
Nice to have
• Refer to "Business Card Details" above.

```html
<!DOCTYPE html>
<html lang="en">
<head>
<meta charset="utf-8">
<title>Copper Ridge Garage Door – Business Cards</title>
<link href="https://fonts.googleapis.com/css2?family=Arimo:wght@400;700&display=swap" rel="stylesheet">
<style>
  :root{
    --navy:#3d4a6b;
    --paper:#f1f1f1;
    --white:#ffffff;
    --ink:#111111;
    --ground:#e4e2de;
  }
  *{box-sizing:border-box;margin:0;padding:0}
  html,body{width:1200px;height:909px;overflow:hidden}
  body{background:var(--ground);font-family:"Arimo",Arial,sans-serif;position:relative}

  .card{position:absolute;left:300px;width:600px;height:343px;border-radius:22px;overflow:hidden;background:var(--paper);box-shadow:0 6px 18px rgba(0,0,0,.18)}
  .card--front{top:92px}
  .card--back{top:474px}

  .brand-seal{position:absolute;border-radius:50%;display:flex;flex-direction:column;align-items:center;justify-content:center;text-align:center;font-weight:700;line-height:1.2;padding:0 28px}
  .brand-seal span{display:block;white-space:nowrap}

  /* front */
  .front-band{position:absolute;left:0;right:0;top:86px;height:128px;background:var(--navy)}
  .card--front .brand-seal{left:170px;top:42px;width:190px;height:190px;background:var(--paper);border:3px solid var(--navy);color:var(--navy);font-size:18px}
  .front-tagline{position:absolute;left:0;right:0;top:250px;text-align:center;color:var(--navy);font-size:24px}
  .front-call{position:absolute;left:0;right:0;top:296px;text-align:center;color:var(--ink);font-size:24px}

  /* back */
  .back-field{position:absolute;left:0;right:0;top:100px;bottom:0;background:var(--navy)}
  .card--back .brand-seal{left:240px;top:14px;width:200px;height:200px;background:var(--navy);border:4px solid var(--white);color:var(--white);font-size:19px}
  .back-tagline{position:absolute;left:0;right:0;top:228px;text-align:center;color:var(--white);font-size:20px}
  .staff{position:absolute;left:24px;top:268px;color:var(--white)}
  .staff-name{font-size:19px;text-transform:uppercase}
  .staff-role{font-size:17px;margin-top:2px}
  .contact-list{position:absolute;left:216px;top:264px;padding-left:12px;border-left:1.5px solid var(--white);list-style:none;color:var(--white);font-size:14px}
  .contact-list li{display:flex;align-items:center;gap:8px;height:16px}
  .contact-list svg{width:11px;height:11px;flex:none}
</style>
</head>
<body>

<section class="card card--front" aria-label="Card front">
  <div class="front-band"></div>
  <div class="brand-seal"><span>COPPER RIDGE</span><span>GARAGE DOOR</span></div>
  <p class="front-tagline">"For All Your Garage Door Needs"</p>
  <p class="front-call">"Call For a FREE Estimate"</p>
</section>

<section class="card card--back" aria-label="Card back">
  <div class="back-field"></div>
  <div class="brand-seal"><span>COPPER RIDGE</span><span>GARAGE DOOR</span></div>
  <p class="back-tagline">"Serving the Greater Metro Denver Area"</p>
  <div class="staff">
    <p class="staff-name">Renata Alvarez</p>
    <p class="staff-role">Project Manager</p>
  </div>
  <ul class="contact-list">
    <li><svg viewBox="0 0 12 12"><rect width="12" height="12" rx="2" fill="#fff"/><path d="M3 3.5h2l.6 1.6-1 .7a5 5 0 0 0 2.6 2.6l.7-1 1.6.6v2A1 1 0 0 1 8.5 9 6 6 0 0 1 3 3.5z" fill="#3d4a6b"/></svg>303.555.0148</li>
    <li><svg viewBox="0 0 12 12"><rect width="12" height="12" rx="2" fill="#fff"/><rect x="2.5" y="3.5" width="7" height="5" fill="none" stroke="#3d4a6b"/><path d="M2.5 3.5 6 6.3 9.5 3.5" fill="none" stroke="#3d4a6b"/></svg>renata@copperridgegarage.example</li>
    <li><svg viewBox="0 0 12 12"><rect width="12" height="12" rx="2" fill="#fff"/><circle cx="6" cy="6" r="3.5" fill="none" stroke="#3d4a6b"/><path d="M2.5 6h7M6 2.5c-2 2-2 5 0 7c2-2 2-5 0-7" fill="none" stroke="#3d4a6b" stroke-width=".8"/></svg>www.copperridgegarage.example</li>
    <li><svg viewBox="0 0 12 12"><rect width="12" height="12" rx="2" fill="#fff"/><path d="M6 10S3 6.8 3 5a3 3 0 0 1 6 0c0 1.8-3 5-3 5z" fill="#3d4a6b"/><circle cx="6" cy="5" r="1" fill="#fff"/></svg>2450 Quarry Lane Suite 210, Lakewood, CO 80215</li>
  </ul>
</section>

</body>
</html>
```